Beacon Advisory Website

I currently have a website www.beaconadvisoryinc.example. We are a IT Consulting Company. Our website will pretty much tell out our services. I am looking to enhance my website and make it look more professional. Looking for very classy and Contemporary look and design for my website.

Industry/Entity Type

It Company

```html
<!DOCTYPE html>
<html lang="en">
<head>
<meta charset="utf-8">
<title>Beacon Advisory – Contact</title>
<link rel="stylesheet" href="https://fonts.googleapis.com/css2?family=Arimo:wght@400;700&display=swap">
<style>
:root{
  --ink:#111111;
  --muted:#a7a7a7;
  --brand:#1c62a5;
  --brand-deep:#0d3f78;
  --paper:#ffffff;
  --map-base:#e6e1d8;
  --map-road:#f2b544;
}
*{margin:0;padding:0;box-sizing:border-box}
html,body{width:1200px;height:675px;overflow:hidden;background:var(--paper)}
body{font-family:"Arimo",Arial,sans-serif;font-weight:700;color:var(--ink);position:relative}
.abs{position:absolute;white-space:nowrap}

.brand{left:20px;top:42px;display:flex;align-items:center;gap:8px}
.brand-dot{width:30px;height:30px;border-radius:50%;background:var(--brand)}
.brand-name{font-size:16px;color:var(--brand-deep);letter-spacing:.5px}

.nav-label{font-size:12px;line-height:16px;color:var(--muted);letter-spacing:.2px}
.nav-link{font-size:13px;line-height:17px;color:var(--brand)}
.nav-item{font-size:13px;line-height:20px;color:var(--ink)}

.plus{left:61px;top:588px;width:24px;height:24px}

.office-title{font-size:20px;line-height:28px;color:var(--muted)}
.office-line{font-size:20px;line-height:28px;color:var(--ink)}

.map{left:766px;top:0;width:434px;height:363px;
  background:linear-gradient(135deg,#e9e4db 0%,var(--map-base) 55%,#ddd8ce 100%)}

.west-title{font-size:13px;line-height:18px}
.west-line{font-size:13px;line-height:22px}
</style>
</head>
<body>

<div class="abs brand"><span class="brand-dot"></span><span class="brand-name">BEACON ADVISORY</span></div>

<nav>
  <div class="abs nav-label" style="left:59px;top:122px">COMPANY</div>
  <div class="abs nav-link" style="left:153px;top:118px">Vision<br>and Mission</div>
  <div class="abs nav-link" style="left:265px;top:118px">Focus</div>

  <div class="abs nav-label" style="left:60px;top:174px">CAREER</div>
  <div class="abs nav-label" style="left:59px;top:211px">CONTACT US</div>

  <div class="abs nav-label" style="left:59px;top:250px">SERVICES</div>
  <div class="abs nav-link" style="left:153px;top:249px">Tecnology</div>
  <div class="abs nav-link" style="left:275px;top:249px">Business</div>
  <div class="abs nav-item" style="left:154px;top:278px">Technologies<br>Training<br>Technology Refresh<br>Capacity on Demand</div>

  <div class="abs nav-label" style="left:58px;top:390px">SOLUTIONS</div>
  <div class="abs nav-link" style="left:154px;top:390px">Dashboards</div>
  <div class="abs nav-link" style="left:275px;top:390px">Data Warehousing</div>
  <div class="abs nav-link" style="left:275px;top:422px;color:var(--ink)">DataMarts and DWH</div>
  <div class="abs nav-link" style="left:275px;top:445px;color:var(--ink)">Extract, Transform<br>And Load</div>

  <div class="abs nav-label" style="left:59px;top:516px">RESOURCES</div>
  <div class="abs nav-link" style="left:153px;top:516px">Our Processs</div>
  <div class="abs nav-link" style="left:277px;top:516px">Staff<br>Augmentation</div>

  <svg class="abs plus" viewBox="0 0 24 24" aria-hidden="true">
    <rect x="10" y="0" width="4" height="24" fill="var(--brand)"/>
    <rect x="0" y="10" width="24" height="4" fill="var(--brand)"/>
  </svg>
</nav>

<section class="abs" style="left:461px;top:223px">
  <div class="office-title">Head Office</div>
  <div class="office-line">410 Harbor Ave</div>
  <div class="office-line">Suite 120</div>
  <div class="office-line">Millbrook, NJ 07999</div>
  <div class="office-line">Phone: +1 (555) 014 2870</div>
</section>

<section class="abs" style="left:461px;top:392px">
  <div class="office-title">Technical Center</div>
  <div class="office-line">2750 Oakridge Road</div>
  <div class="office-line">Suite 340</div>
  <div class="office-line">Cedar Falls MI 49999</div>
</section>

<div class="abs map" role="img" aria-label="Street map showing the technical center location at 2750 Oakridge Rd #340"></div>

<section class="abs" style="left:767px;top:516px">
  <div class="west-title">West Coast Office</div>
  <div class="west-line" style="margin-top:25px">880 Summit Place</div>
  <div class="west-line">Suite 500</div>
  <div class="west-line">Lakeview, CA 95999</div>
</section>

</body>
</html>
```